Australia-based Training Business needs bilingual brochure design

I need to design a brochure to promote our upcoming training workshops. It needs to be bilingual (in Chinese and English). I'd prefer the brochure to be 2-fold A5 (4 pages, color), but 3 fold pamphlet (6 pages) is also OK if necessary.
I have already attached the content, logo (two versions) and photos to be included in the brochure. Pls also check my website www.dulvora.com.au for the kind of style I like (although I'm open for suggestions).
I will need the design in as soon as possible. I like modern clean looking designs with appealing images which are not over-powering the content. If the content needs to be cut down, I am happy to do so, just send me a draft design so I know how words to cut. Thank you!
Target Market(s)
Chinese-background professionals, small business owners working in Australia.
Industry/Entity Type
Training
Requirements
Must have
- Inviting pictures, logo, some relevant images, photos (people attending business training).
Nice to have
- elements of Chinese & Australia culture
- trainers photos
Should not have
- boring pictures

```html
<!DOCTYPE html>
<html lang="en">
<head>
<meta charset="utf-8">
<title>Dulvora Business Education – Brochure</title>
<link rel="stylesheet" href="https://fonts.googleapis.com/css2?family=Oswald:wght@500;700&family=Open+Sans:wght@400;700&display=swap">
<style>
  :root {
    --brown: #4b2f28;
    --brown-deep: #3e2620;
    --orange: #f5a11c;
    --white: #ffffff;
    --panel-grey: #e8e5e3;
    --stage: #f2ece7;
    --ink: #2e1d18;
  }
  * { box-sizing: border-box; margin: 0; padding: 0; }
  html, body { width: 1200px; height: 807px; overflow: hidden; }
  body { background: var(--stage); font-family: "Open Sans", Arial, sans-serif; }

  .spread { position: absolute; left: 92px; top: 44px; width: 1016px; height: 720px; display: flex; box-shadow: 0 10px 30px rgba(60,35,25,.25); }
  .page { position: relative; width: 508px; height: 720px; overflow: hidden; }

  /* Back page */
  .page--back { background: var(--brown); color: var(--white); }
  .back-photo { position: absolute; left: 0; top: 0; width: 508px; height: 272px;
    background: linear-gradient(160deg, #eef3f8 0%, #b9cbe0 40%, #3f5f86 75%, #1f3450 100%); }
  .back-edge { position: absolute; left: 0; top: 0; }
  .about { position: absolute; left: 48px; top: 292px; width: 412px; font-size: 12.5px; line-height: 1.38; text-align: justify; }
  .about p + p { margin-top: 10px; }
  .services { position: absolute; left: 74px; top: 474px; width: 360px; padding: 8px 14px 10px; background: var(--panel-grey); border: 3px solid var(--orange); color: var(--ink); font-size: 12.5px; line-height: 1.35; }
  .services h3 { text-align: center; font-size: 13px; font-weight: 700; margin-bottom: 3px; }
  .services ol { padding-left: 22px; }
  .enquiries-title { position: absolute; left: 0; top: 596px; width: 100%; text-align: center; font-family: "Oswald", Arial, sans-serif; font-weight: 500; font-size: 20px; line-height: 26px; letter-spacing: .5px; }
  .contact-band { position: absolute; left: 0; width: 100%; height: 36px; background: var(--orange); display: flex; align-items: center; justify-content: center; gap: 8px; font-family: "Oswald", Arial, sans-serif; font-weight: 500; font-size: 15px; letter-spacing: 1.5px; color: var(--white); white-space: nowrap; }
  .page--back .contact-band { top: 628px; gap: 6px; font-size: 13px; letter-spacing: 1px; }
  .contact-band .sep { opacity: .9; }
  .icon { display: inline-block; vertical-align: middle; flex: none; }
  .chat-dot { width: 12px; height: 12px; border-radius: 50%; background: var(--white); display: inline-block; flex: none; }
  .website { position: absolute; left: 0; width: 100%; text-align: center; font-family: "Oswald", Arial, sans-serif; font-weight: 500; font-size: 17px; line-height: 24px; letter-spacing: 3px; color: var(--white); }
  .page--back .website { top: 676px; }

  /* Front page */
  .page--front { background: var(--white); }
  .front-header { position: absolute; left: 0; top: 0; }
  .brand { position: absolute; left: 0; top: 18px; width: 100%; display: flex; justify-content: center; align-items: center; gap: 10px; }
  .brand-mark { width: 26px; height: 26px; background: var(--orange); }
  .brand-name { font-family: "Oswald", Arial, sans-serif; font-weight: 500; font-size: 17px; line-height: 1.05; color: var(--white); text-transform: uppercase; letter-spacing: .5px; }
  .headline { position: absolute; left: 0; top: 98px; width: 100%; text-align: center; font-family: "Oswald", Arial, sans-serif; font-weight: 700; font-size: 50px; line-height: 1.02; text-transform: uppercase; color: var(--brown); }
  .headline .accent { color: var(--orange); font-size: 40px; }
  .front-photo { position: absolute; left: 0; top: 210px; width: 508px; height: 408px;
    background: linear-gradient(180deg, #ffffff 0%, #f1f1f3 35%, #c9ced9 55%, #b27a55 78%, #5a3a2b 100%); }
  .tagline { position: absolute; right: 34px; top: 232px; width: 250px; font-family: "Oswald", Arial, sans-serif; font-weight: 700; font-size: 33px; line-height: 1.05; text-transform: uppercase; color: var(--brown); text-align: left; }
  .tagline .accent { color: var(--orange); font-size: 27px; }
  .page--front .contact-band { top: 614px; height: 40px; }
  .front-footer { position: absolute; left: 0; top: 654px; width: 100%; height: 66px; background: var(--brown); }
  .page--front .website { top: 670px; }
</style>
</head>
<body>
  <main class="spread">
    <section class="page page--back">
      <div class="back-photo" role="img" aria-label="Photo of a trainer presenting to a large seated audience in a bright seminar room"></div>
      <svg class="back-edge" width="508" height="300" viewBox="0 0 508 300" aria-hidden="true">
        <polygon points="0,256 222,256 254,280 286,256 508,256 508,300 0,300" fill="var(--brown)"/>
        <polyline points="0,256 222,256 254,280 286,256 508,256" fill="none" stroke="var(--orange)" stroke-width="4"/>
      </svg>

      <div class="about">
        <p>Dulvora Business Education (DBE) is a Sydney-based corporate training provider servicing Chinese Australian business professionals and executives.</p>
        <p>All trainers at DBE are experienced practitioners who have had successful corporate careers, passionate about sharing their knowledge AND skilled in delivering optimum training outcome.</p>
        <p>Our workshops are run in small group, highly interactive, and packed with information and tips. As a bonus, you will also meet guest senior executives from leading Australian organisation at each workshop.</p>
      </div>

      <div class="services">
        <h3>We also provide:</h3>
        <ol>
          <li>1-2 days in-house corporate training programs in Cross-Cultural Negotiation and Communication.</li>
          <li>5-day NORVA/IPSC Certificate Training programs in Procurement Management in English and Chinese.</li>
        </ol>
      </div>

      <h2 class="enquiries-title">ENROLMENT AND ENQUIRIES:</h2>
      <div class="contact-band">
        <svg class="icon" width="13" height="13" viewBox="0 0 24 24" aria-hidden="true"><path fill="#fff" d="M6.6 10.8a15 15 0 0 0 6.6 6.6l2.2-2.2a1 1 0 0 1 1-.25 11.4 11.4 0 0 0 3.6.57 1 1 0 0 1 1 1V20a1 1 0 0 1-1 1A17 17 0 0 1 3 4a1 1 0 0 1 1-1h3.5a1 1 0 0 1 1 1c0 1.25.2 2.45.57 3.57a1 1 0 0 1-.25 1z"/></svg>
        <span>0400 512 874</span><span class="sep">|</span>
        <svg class="icon" width="15" height="11" viewBox="0 0 16 12" aria-hidden="true"><rect x="0" y="0" width="16" height="12" fill="#fff"/><polyline points="0,0 8,7 16,0" fill="none" stroke="var(--orange)" stroke-width="1.5"/></svg>
        <span>MIRA@DULVORA.COM.AU</span><span class="sep">|</span>
        <span class="chat-dot" aria-hidden="true"></span>
        <span>ID: MIRAINSYDNEY</span>
      </div>
      <p class="website">WWW.DULVORA.COM.AU</p>
    </section>

    <section class="page page--front">
      <div class="front-photo" role="img" aria-label="Photo of a smiling trainer in shirt and tie gesturing towards a board in front of a seated audience seen from behind"></div>

      <svg class="front-header" width="508" height="100" viewBox="0 0 508 100" aria-hidden="true">
        <polygon points="0,0 508,0 508,70 284,70 254,94 224,70 0,70" fill="var(--brown)"/>
        <polyline points="0,70 224,70 254,94 284,70 508,70" fill="none" stroke="var(--orange)" stroke-width="3"/>
      </svg>
      <div class="brand">
        <span class="brand-mark" aria-hidden="true"></span>
        <span class="brand-name">Dulvora<br>Business Education</span>
      </div>

      <h1 class="headline"><span class="accent">Dulvora</span> Business<br><span class="accent">Education</span></h1>

      <p class="tagline"><span class="accent">We</span> help you <span class="accent">to</span><br>stand out <span class="accent">from</span><br><span class="accent">the</span> crowd!</p>

      <div class="contact-band">
        <svg class="icon" width="16" height="12" viewBox="0 0 16 12" aria-hidden="true"><rect x="0" y="0" width="16" height="12" fill="#fff"/><polyline points="0,0 8,7 16,0" fill="none" stroke="var(--orange)" stroke-width="1.5"/></svg>
        <span>MIRA@DULVORA.COM.AU</span><span class="sep">|</span>
        <span class="chat-dot" aria-hidden="true"></span>
        <span>ID: MIRAINSYDNEY</span>
      </div>
      <div class="front-footer"></div>
      <p class="website">WWW.DULVORA.COM.AU</p>
    </section>
  </main>
</body>
</html>
```